依頼詳細
(1)ポスターの概要
ポスターは別途、A1もしくはA2で印刷し、ラミネート加工した上で、ポスター立てに設置。商店街を通る通行客に対して、①アイキャッチ(美味しいぬか漬けや惣菜などがあること)、②70年の伝統がある八百屋であること、を訴求します。つなり、(a)通行客の足を留めるインパクト、(b)足を止めた人に伝統があり、美味しい商品がある「食べてみたい!」という印象をもってもらえること、が目的です。その(a)(b)を満たすようなポスターデザインを希望します。活用方法としては、そのほかにA4サイズでPOPとして利用することも検討しています。

(2)留意点
尚、貼付写真はスマホで撮影しており、画素数がそれほど高くないことは承知しております。画素数の兼ね合いで写真の大きさなども変わってきたり、あるいは、A1で印刷する場合、粗い画像になるなどのリスクがあるかと思いますが、そのあたりも見え方によりけりかと考えますんどえ、フレキシブルに対応いただけると幸いです。

(3)お願い
①70年以上続く昔ながらの伝統ある八百屋さん、②美味しい野菜や総菜にこだわっている、③上記のこれから頑張っていこうとする3代目の意欲、などが感覚的に伝わるようなデザインを希望いたします。
記載項目
(1)社名「青果竹」

(2)ショルダーネーム
大田区蒲田の人々と共に歩んできた八百屋
蒲田で創業 昭和23年

(3)電話番号「03-5820-4417」

(4)キャッチコピー「70年の菌を味わう」

(5)写真
①ぬか床(貼付ファイル1枚)
②きゅうりのぬか漬け(貼付ファイル3枚)
③なすのぬか漬け(貼付ファイル1枚)
④梅干し(貼付ファイル1枚)
⑤焼き芋(貼付ファイル1枚)
⑥惣菜(貼付ファイル2枚)
⑦大根・カブのぬか漬け(貼付ファイル1枚)

・上記の①②③のどれか(良いと思われるもの)を大きく。
・その他は小さく。
・複数枚あるのは良いと思われるものを選定してください。

(6)コメント
「創業当初から、「糠は生きもの」という創業者の意思を継ぎ、
いまだに継ぎ足しながら育ててきた70年酵母の
素朴ながら深みのある味のお漬物です」
■ 選んだ理由

70年の菌を味わうというキャッチコピーを最優先に考えていただいた点、特に「70」という数字が最初に飛び込んでくる点が最も大きな選定理由です。また、黒を基調としたイメージが、歴史があるということを強調する重厚感に繋がっている点や、遠目からのアイキャッチとして機能しそうだと感じた点が選定理由として大きいです。他の作品も甲乙つけがたい部分もありましたが、最終的には当事者である青果竹さんの経営陣が直感的に良いと感じたことで決定にいたりました。

■ 提案者全員のお礼・コメント

皆さま、本当にたいくさんの力作ぞろいの提案をありがとうございました。青果竹の経営者からは、「どの作品も当社のことを考えてくださっていることがわかるデザインで、一つに絞りに切れない」という本音が出ていました。これからも折に触れて、ポスターをリニューアルしていきたいと考えておりますので、お付き合いの程、よろしくお願いいたします。ぜひ、店頭にいらっしゃた際には、「ポスターデザインを提案しました」と一声お声がけいただけますと幸いです。

```html
<!DOCTYPE html>
<html lang="ja">
<head>
<meta charset="utf-8">
<title>青果竹 ポスター</title>
<link rel="stylesheet" href="https://fonts.googleapis.com/css2?family=Shippori+Mincho:wght@500;700&display=swap">
<style>
  :root {
    --pink: #f4d9dc;
    --cream: #f4ecd6;
    --green: #dfeecf;
    --lavender: #eadcf0;
    --paper: #fdfcfa;
    --ink: #2a2623;
    --red: #c2342d;
    --plum: #b5434f;
    --radish: #d9c39a;
    --cucumber: #5b6e3a;
    --eggplant: #3b3f66;
  }
  html, body { margin: 0; padding: 0; overflow: hidden; }
  body { width: 846px; height: 1200px; background: var(--paper); }
  .poster {
    position: relative; width: 846px; height: 1200px; overflow: hidden;
    font-family: "Shippori Mincho", serif; color: var(--ink); background: var(--paper);
  }
  .block { position: absolute; width: 423px; height: 300px; }
  .block--pink { left: 0; top: 0; background: var(--pink); }
  .block--cream { left: 423px; top: 0; background: var(--cream); }
  .block--green { left: 0; top: 300px; background: var(--green); }
  .block--lavender { left: 423px; top: 300px; background: var(--lavender); }

  .photo { position: absolute; }
  .photo--plum { left: 30px; top: 28px; width: 180px; height: 145px; }
  .photo--radish { left: 495px; top: 28px; width: 300px; height: 240px; }
  .photo--cucumber { left: 42px; top: 340px; width: 285px; height: 240px; }
  .photo--eggplant { left: 508px; top: 370px; width: 295px; height: 210px; }

  .headline {
    position: absolute; left: 376px; top: 80px;
    writing-mode: vertical-rl; font-size: 40px; font-weight: 700;
    letter-spacing: 0.25em; line-height: 1; margin: 0;
  }
  .story {
    position: absolute; right: 50px; top: 650px;
    writing-mode: vertical-rl; font-size: 20px; font-weight: 500;
    line-height: 1.15; letter-spacing: 0.6em; margin: 0;
  }
  .shop {
    position: absolute; left: 14px; top: 975px; width: 142px; height: 212px;
    background: #fff; color: var(--red);
  }
  .shop__shoulder {
    position: absolute; right: 12px; top: 14px; margin: 0;
    writing-mode: vertical-rl; font-size: 12px; line-height: 1.6; letter-spacing: 0.06em;
  }
  .shop__tel {
    position: absolute; right: 56px; top: 14px; margin: 0;
    writing-mode: vertical-rl; font-size: 11px; letter-spacing: 0.04em;
  }
  .shop__name {
    position: absolute; left: 14px; top: 90px; width: 44px; height: 110px;
    border: 2px solid var(--red); box-sizing: border-box;
    writing-mode: vertical-rl; font-size: 24px; font-weight: 700;
    display: flex; align-items: center; justify-content: center; margin: 0;
  }
</style>
</head>
<body>
<div class="poster">
  <div class="block block--pink"></div>
  <div class="block block--cream"></div>
  <div class="block block--green"></div>
  <div class="block block--lavender"></div>

  <svg class="photo photo--plum" viewBox="0 0 180 145" role="img" aria-label="梅干しの写真">
    <ellipse cx="90" cy="72" rx="88" ry="70" fill="var(--plum)" opacity="0.85"/>
  </svg>
  <svg class="photo photo--radish" viewBox="0 0 300 240" role="img" aria-label="大根とカブのぬか漬けの写真">
    <ellipse cx="150" cy="120" rx="148" ry="115" fill="var(--radish)" opacity="0.9"/>
  </svg>
  <svg class="photo photo--cucumber" viewBox="0 0 285 240" role="img" aria-label="きゅうりのぬか漬けの写真">
    <ellipse cx="142" cy="120" rx="140" ry="115" fill="var(--cucumber)" opacity="0.85"/>
  </svg>
  <svg class="photo photo--eggplant" viewBox="0 0 295 210" role="img" aria-label="なすのぬか漬けの写真">
    <ellipse cx="147" cy="105" rx="144" ry="100" fill="var(--eggplant)" opacity="0.88"/>
  </svg>

  <h1 class="headline">七十年の菌を味わう。</h1>

  <p class="story">昭和二十三年の<br>創業当初から<br>「糠は生きもの」という<br>創業者の意思を継ぎ、<br>いまだに継ぎ足しながら<br>育ててきた<br>70年酵母の<br>素朴ながら<br>深みのある味の<br>お漬物です。</p>

  <div class="shop">
    <p class="shop__shoulder">蒲田の人々と<br>共に歩んできた八百屋</p>
    <p class="shop__tel">☎03-5820-4417</p>
    <p class="shop__name">青果竹</p>
  </div>
</div>
</body>
</html>
```